Elegant and modern body scrub for organic junkies

I need a package design for my new company based out of Austin, Texas. We are focused on cruelty free and all natural and organic products. Our deign needs to be able to have the information we require on it, while still appearing very clean and captivating. Our initial product is a clear skin body scrub, intended for people with problematic skin. Our target market is women and we want to show elegance, without appearing "high end."
Updates

Reason: I want to allot more time for certain designers to submit edits. Last minute proposals have been appealing

Target Market(s)

Women. Organic and holistic minded. Natural beauty lovers.

Industry/Entity Type

Skin Care Product

Font styles to use
Script
Other font styles liked:
• AmericanTypewriter, Beautifulflaws, courier, caviarDreams-bold

Colors
000000
ffc214
ffffff
fece3e
fbee3e

Requirements
Must have
• Must be designed in Adobe Illustrator.
• The photo titled “structure for oz and grams” -That needs to be included at the bottom of 1B. I like the horizontal and vertical bar that separate the two. I want that.
• Color Inspiration - The photo titled “venra color inspiration” and “color combo inspiration” are the colors I want. BLACK, GOLD, WHITE. I want the label background black and the writing in white with some gold somewhere on it. My logo is going to be a Amber Grove.
• The photos titled “I like how clean this looks” and “I also like how clean this looks” - I want 1B to look super clean. I don’t want a lot of information in this box. I want simple and clean. This is where the logo and brand name will go.
• Logo - A Amber Grove. I want it to be gold and geometric. There can be dimension like this elephant example on the left of the 1B description. I want the trunk to be facing to the left and the trunk needs to be raised overhead and touching the animal's forehead.
• The photo titled “sideways writing and silver rim” - I want 1C to be written sideways like this. My text will be much more extensive so the font won’t be able to be so big.
Nice to have
• The photo titled “sideways writing and silver rim” - I want 1C to be written sideways like this. My text will be much more extensive so the font won’t be able to be so big. I also REALLY like how this label is rimmed in silver, but I would want gold. This is not mandatory, but I really like this.
• The photo titled “melted honey” - This is another option I really like. The gold that looks like honey dripping on the label is really cool. Not mandatory, but I really liked that. I also like the craft background on this.
• Color Inspiration - The photo titled “color inspiration” and “another color inspiration” is an option I would also like to see. Rather than black, I’d like to see what it would ALSO look like with a navy background. NAVY, GOLD, WHITE, maybe black somewhere.
Should not have
• Colorful patterns or excessive info in section 1B.

```html
<!DOCTYPE html>
<html lang="en">
<head>
<meta charset="utf-8">
<title>Amber Grove – Clear Skin Body Polish Label</title>
<link rel="stylesheet" href="https://fonts.googleapis.com/css2?family=Montserrat:wght@300;400;700&display=swap">
<style>
  :root {
    --page: #ffffff;
    --label-dark: #0c0c0c;
    --label-edge: #343434;
    --gold-light: #f3c955;
    --gold: #d9a431;
    --gold-deep: #b87a18;
    --text: #ffffff;
  }
  * { margin: 0; padding: 0; box-sizing: border-box; }
  html, body {
    width: 1200px;
    height: 1200px;
    overflow: hidden;
    background: var(--page);
    font-family: "Montserrat", sans-serif;
  }
  .canvas {
    position: relative;
    width: 1200px;
    height: 1200px;
  }
  .label {
    position: absolute;
    left: 100px;
    top: 366px;
    width: 1000px;
    height: 468px;
    background: linear-gradient(90deg, var(--label-edge) 0%, var(--label-dark) 45%, var(--label-dark) 70%, var(--label-edge) 100%);
    overflow: hidden;
  }
  .honey-drip {
    position: absolute;
    left: 166px;
    top: 0;
    width: 680px;
    height: 118px;
    background: linear-gradient(180deg, var(--gold-light) 0%, var(--gold) 55%, var(--gold-deep) 100%);
    border-radius: 0 0 40px 40px;
  }
  .brand-mark {
    position: absolute;
    left: 412px;
    top: 146px;
    width: 132px;
    height: 132px;
    border-radius: 50%;
    background: linear-gradient(135deg, var(--gold-light), var(--gold-deep));
  }
  .brand-name {
    position: absolute;
    left: 0;
    right: 0;
    top: 318px;
    text-align: center;
    color: var(--text);
    font-weight: 700;
    font-size: 29px;
    letter-spacing: 0.52em;
    padding-left: 0.52em;
  }
  .rule {
    position: absolute;
    left: 186px;
    top: 367px;
    width: 584px;
    height: 2px;
    background: var(--gold);
  }
  .product-line {
    position: absolute;
    left: 186px;
    top: 376px;
    width: 584px;
    display: flex;
    align-items: stretch;
    justify-content: space-between;
    color: var(--text);
    font-weight: 300;
    font-size: 18px;
    letter-spacing: 0.36em;
    line-height: 1;
  }
  .product-line span {
    padding: 10px 0;
  }
  .divider {
    width: 2px;
    background: var(--gold);
    padding: 0 !important;
  }
</style>
</head>
<body>
  <main class="canvas">
    <section class="label">
      <div class="honey-drip" role="img" aria-label="Melted gold honey dripping down from the top edge of the label"></div>
      <div class="brand-mark" aria-hidden="true"></div>
      <h1 class="brand-name">AMBER GROVE</h1>
      <div class="rule"></div>
      <p class="product-line">
        <span class="product-type">CLEAR SKIN BODY POLISH</span>
        <span class="divider"></span>
        <span class="weight-oz">12oz</span>
        <span class="divider"></span>
        <span class="weight-g">340g</span>
      </p>
    </section>
  </main>
</body>
</html>
```